Working Capital graphics

Our business advisory firm requires 9 images to be re-created and improved in the branding of our business.

The 9 images have been uploaded below and the colours and branding of the business can be found at the website www.thornwickadvisory.com.au

```html
<!DOCTYPE html>
<html lang="en">
<head>
<meta charset="utf-8">
<title>Working K in the Value Chain</title>
<link rel="stylesheet" href="https://fonts.googleapis.com/css2?family=Lato:ital,wght@0,400;0,700;0,900;1,900&display=swap">
<style>
  :root {
    --navy: #0d2344;
    --orange: #f7941d;
    --cyan: #00aeef;
    --paper: #ffffff;
  }
  * { box-sizing: border-box; margin: 0; padding: 0; }
  html, body { width: 1200px; height: 960px; overflow: hidden; background: var(--paper); }
  body { font-family: "Lato", Arial, sans-serif; color: var(--navy); }
  .canvas { position: relative; width: 1200px; height: 960px; }

  .title {
    position: absolute; left: 80px; top: 82px;
    font-size: 38px; font-weight: 900; font-style: italic;
    letter-spacing: 3px; color: var(--navy);
  }

  .chain { position: absolute; left: 0; top: 0; }

  .lever {
    position: absolute; width: 152px; height: 92px;
    border: 3px solid var(--navy); border-radius: 12px;
    display: flex; align-items: center; justify-content: center;
    text-align: center; font-weight: 700; font-size: 17px; line-height: 21px;
    text-transform: uppercase; background: var(--paper);
  }
  .lever--payables { border-color: var(--orange); }
  .lever--receivables { border-color: var(--navy); }
  .lever--small { font-size: 15px; line-height: 18px; }

  .stage-label {
    position: absolute; top: 525px; transform: translate(-50%, -50%);
    text-align: center; font-weight: 700; text-transform: uppercase;
    font-size: 18px; line-height: 21px; white-space: nowrap;
  }
  .stage-label--sm { font-size: 15px; line-height: 18px; }
  .stage-label--xs { font-size: 11px; }
  .stage-label--md { font-size: 14px; }

  .legend { position: absolute; top: 864px; display: flex; align-items: center; gap: 12px; }
  .legend__swatch { width: 30px; height: 30px; border: 3px solid; border-radius: 6px; }
  .legend__text { font-weight: 700; font-size: 18px; line-height: 21px; text-transform: uppercase; }

  .brand { position: absolute; left: 56px; top: 858px; display: flex; align-items: center; gap: 12px; }
  .brand__dot { width: 44px; height: 44px; border-radius: 50%; background: var(--orange); }
  .brand__name { font-weight: 400; font-size: 19px; line-height: 21px; letter-spacing: 1px; color: var(--navy); text-transform: uppercase; }
</style>
</head>
<body>
<main class="canvas">
  <h1 class="title">WORKING K IN THE VALUE CHAIN</h1>

  <svg class="chain" width="1200" height="960" viewBox="0 0 1200 960" aria-hidden="true">
    <g fill="none" stroke-width="3">
      <!-- connectors -->
      <g stroke="var(--orange)">
        <line x1="126" y1="414" x2="126" y2="468"/>
        <polyline points="502,414 502,439 225,439 225,468"/>
        <line x1="343" y1="582" x2="343" y2="623"/>
        <line x1="744" y1="414" x2="744" y2="468"/>
        <line x1="911" y1="582" x2="911" y2="623"/>
        <line x1="1051" y1="582" x2="1051" y2="623"/>
      </g>
      <g stroke="var(--navy)">
        <line x1="343" y1="297" x2="343" y2="322"/>
        <line x1="343" y1="414" x2="343" y2="468"/>
        <line x1="911" y1="297" x2="911" y2="322"/>
        <line x1="911" y1="414" x2="911" y2="468"/>
        <line x1="1051" y1="414" x2="1051" y2="468"/>
      </g>
      <!-- value chain stages -->
      <g stroke="var(--cyan)" stroke-width="2.6" stroke-linejoin="miter">
        <polygon points="47,468 161,468 181,525 161,582 47,582"/>
        <polygon points="170,468 277,468 298,525 277,582 170,582 191,525"/>
        <polygon points="287,468 394,468 415,525 394,582 287,582 308,525"/>
        <polygon points="404,468 511,468 532,525 511,582 404,582 425,525"/>
        <polygon points="522,468 629,468 650,525 629,582 522,582 543,525"/>
        <polygon points="639,468 746,468 767,525 746,582 639,582 660,525"/>
        <polygon points="756,468 863,468 884,525 863,582 756,582 777,525"/>
        <polygon points="873,468 980,468 1001,525 980,582 873,582 894,525"/>
        <polygon points="999,468 1110,468 1132,525 1110,582 999,582 1020,525"/>
      </g>
    </g>
  </svg>

  <span class="stage-label" style="left:114px">Design</span>
  <span class="stage-label" style="left:240px">Order/<br>Material<br>Planning</span>
  <span class="stage-label stage-label--sm" style="left:361px;font-size:17px">Purchasing</span>
  <span class="stage-label stage-label--xs" style="left:476px">Manufacturing</span>
  <span class="stage-label stage-label--md" style="left:595px">Pre-Assembly</span>
  <span class="stage-label" style="left:713px">Assembly</span>
  <span class="stage-label stage-label--sm" style="left:827px">Packaging/<br>Shipping</span>
  <span class="stage-label" style="left:936px">Sales</span>
  <span class="stage-label stage-label--sm" style="left:1072px">After Sales/<br>Service</span>

  <div class="lever lever--receivables" style="left:261px;top:205px">Modify<br>Payment<br>Conditions</div>
  <div class="lever lever--receivables" style="left:835px;top:205px">Improve<br>Payment<br>Schemes</div>

  <div class="lever lever--payables" style="left:50px;top:322px">Reduce Part<br>Variants/<br>Releases</div>
  <div class="lever lever--receivables" style="left:261px;top:322px">Optimize<br>Payment<br>Process</div>
  <div class="lever lever--payables lever--small" style="left:426px;top:322px">Rethink Delivery<br>Schedules and<br>Warehousing</div>
  <div class="lever lever--payables" style="left:668px;top:322px">Optimize<br>Product<br>Testing</div>
  <div class="lever lever--receivables" style="left:835px;top:322px">Reduce Due/<br>Overdue<br>Receivables</div>
  <div class="lever lever--receivables lever--small" style="left:1000px;top:322px">Establish New<br>Payment<br>Conditions</div>

  <div class="lever lever--payables" style="left:265px;top:623px">Optimize<br>External<br>Purchasing</div>
  <div class="lever lever--payables" style="left:831px;top:623px">Reduce<br>Finished<br>Goods Stocks</div>
  <div class="lever lever--payables" style="left:985px;top:623px">Reduce<br>Inventory</div>

  <div class="brand">
    <span class="brand__dot"></span>
    <span class="brand__name">Thornwick<br>Advisory</span>
  </div>

  <div class="legend" style="left:455px">
    <span class="legend__swatch" style="border-color:var(--cyan)"></span>
    <span class="legend__text">Inventory</span>
  </div>
  <div class="legend" style="left:626px">
    <span class="legend__swatch" style="border-color:var(--orange)"></span>
    <span class="legend__text">Payables and<br>Prepayments Made</span>
  </div>
  <div class="legend" style="left:876px">
    <span class="legend__swatch" style="border-color:var(--navy)"></span>
    <span class="legend__text">Receivables and<br>Prepayments Received</span>
  </div>
</main>
</body>
</html>
```